High end Electrical/home automation Business Card

Need a card for a high end electrical and home automation company utilising the existing logo.
Phone
Email
Website

Like black look with raised detail. Don’t necessarily need to keep colour of logo it could be made grayscale or white etc

Target Market(s)

High end clients

Contact Information for Business Card

Ridgeline Electrical

Requirements
Must have
• Logo, phone, email, website, address

High end look
Nice to have
• Black background card
Raised font
Should not have
• Lots of colour

```html
<!DOCTYPE html>
<html lang="en">
<head>
<meta charset="utf-8">
<title>Ridgeline Electrical — Business Card</title>
<link href="https://fonts.googleapis.com/css2?family=Montserrat:wght@800&family=Arimo:wght@400;700&display=swap" rel="stylesheet">
<style>
  :root{
    --stage:#e9eaec;
    --card-dark:#2f3236;
    --card-dark-edge:#3a3e43;
    --glow:#1690d6;
    --card-light:#ffffff;
    --ink:#2c2c2e;
    --ink-soft:#3d3d40;
    --accent:#1a95dc;
    --accent-2:#2ea7e6;
    --white:#ffffff;
  }
  *{margin:0;padding:0;box-sizing:border-box}
  html,body{width:1200px;height:900px;overflow:hidden;background:var(--stage)}
  .stage{position:relative;width:1200px;height:900px}
  .card{position:absolute;left:285px;width:630px;height:360px;border-radius:22px;overflow:hidden;box-shadow:0 10px 30px rgba(0,0,0,.18)}

  /* back side */
  .card--back{top:50px;background:radial-gradient(ellipse 55% 60% at 52% 42%, var(--glow) 0%, #175f8c 38%, var(--card-dark-edge) 72%, var(--card-dark) 100%)}
  .back__brand{position:absolute;left:0;right:0;top:140px;display:flex;align-items:center;justify-content:center;gap:16px}
  .back__dot{width:22px;height:22px;border-radius:50%;background:var(--white)}
  .back__name{font-family:"Montserrat",sans-serif;font-weight:800;font-size:40px;color:var(--white);letter-spacing:.5px}
  .back__web{position:absolute;left:0;right:0;top:232px;text-align:center;font-family:"Arimo",sans-serif;font-size:15px;letter-spacing:5px;color:var(--white)}

  /* front side */
  .card--front{top:490px;background:var(--card-light)}
  .front__brand{position:absolute;right:44px;top:52px;display:flex;align-items:center;gap:12px}
  .front__dot{width:18px;height:18px;border-radius:50%;background:var(--accent)}
  .front__name{font-family:"Montserrat",sans-serif;font-weight:800;font-size:30px;color:var(--ink)}
  .person{position:absolute;right:44px;top:112px;font-family:"Arimo",sans-serif;font-weight:700;font-size:30px;color:var(--accent);text-align:right}
  .rule{position:absolute;left:30px;top:170px;width:420px;height:1.5px;background:var(--ink)}
  .role{position:absolute;right:44px;top:160px;font-family:"Arimo",sans-serif;font-size:20px;color:var(--ink-soft)}
  .address{position:absolute;right:44px;top:198px;font-family:"Arimo",sans-serif;font-size:20px;line-height:1.35;color:var(--ink-soft);text-align:right}
  .contacts{position:absolute;left:34px;top:196px;list-style:none;font-family:"Arimo",sans-serif;font-size:18px;color:var(--ink)}
  .contacts li{display:flex;align-items:center;gap:10px;height:28px}
  .contacts svg{width:15px;height:15px;flex:none}
  .contacts .link{color:var(--accent)}
  .band{position:absolute;left:0;bottom:0;width:630px;height:40px}
</style>
</head>
<body>
<main class="stage">
  <section class="card card--back" aria-label="Card back">
    <div class="back__brand">
      <span class="back__dot"></span>
      <span class="back__name">Ridgeline Electrical</span>
    </div>
    <p class="back__web">www.ridgelineelectrical.com</p>
  </section>

  <section class="card card--front" aria-label="Card front">
    <div class="front__brand">
      <span class="front__dot"></span>
      <span class="front__name">Ridgeline Electrical</span>
    </div>
    <p class="person">Daniel Hartley</p>
    <div class="rule"></div>
    <p class="role">Manager</p>
    <p class="address">Your address, city<br>state, ZIP 0000</p>
    <ul class="contacts">
      <li>
        <svg viewBox="0 0 16 16"><path d="M4 1.5c1 0 1.5 2.8 1 3.4L3.9 6c.8 2 2.2 3.4 4.1 4.2l1.1-1.1c.6-.5 3.4 0 3.4 1 0 1.3-1 3.4-2.6 3.4C5.5 13.5 2.5 10.5 2.5 4.1 2.5 2.5 2.7 1.5 4 1.5z" fill="var(--accent)"/></svg>
        <span>555-014-2100</span>
      </li>
      <li>
        <svg viewBox="0 0 16 16"><rect x="1.5" y="3.5" width="13" height="9" rx="1" fill="none" stroke="var(--accent)" stroke-width="1.4"/><path d="M1.8 4l6.2 5 6.2-5" fill="none" stroke="var(--accent)" stroke-width="1.4"/></svg>
        <span>hello@ridgelinemail.com</span>
      </li>
      <li>
        <svg viewBox="0 0 16 16"><circle cx="8" cy="8" r="6.3" fill="none" stroke="var(--accent)" stroke-width="1.4"/><ellipse cx="8" cy="8" rx="2.8" ry="6.3" fill="none" stroke="var(--accent)" stroke-width="1.2"/><path d="M1.8 8h12.4M2.8 5h10.4M2.8 11h10.4" stroke="var(--accent)" stroke-width="1.1"/></svg>
        <span>www.<span class="link">ridgelineelectrical</span>.com</span>
      </li>
    </ul>
    <svg class="band" viewBox="0 0 630 40" preserveAspectRatio="none" aria-hidden="true">
      <polygon points="250,14 268,14 248,40 230,40" fill="var(--card-dark)"/>
      <polygon points="278,4 630,4 630,40 256,40" fill="var(--accent-2)"/>
    </svg>
  </section>
</main>
</body>
</html>
```